Brambury Logistics

Create a modern, simple, Elegant business card design for my business.

Services: Tamo Trucks, Transport, Contract Logistics,

Industry/Entity Type

Business

Contact Information for Business Card

Include all details same as old card plus new website address: www.bramburylogistics.com.au

Requirements
Must have
• Similar colors to Logo.

```html
<!DOCTYPE html>
<html lang="en">
<head>
<meta charset="utf-8">
<title>Brambury Logistics – Business Card</title>
<link rel="stylesheet" href="https://fonts.googleapis.com/css2?family=Roboto:wght@400;500&display=swap">
<style>
  :root {
    --backdrop: #d9d4cc;
    --card-top: #f3f5f7;
    --card-top-edge: #e3e8ed;
    --band-grey-light: #8e8e90;
    --band-grey-dark: #4f4f52;
    --blue-light: #3f86a6;
    --blue-dark: #0e3553;
    --logo-ink: #3a3d42;
    --name-ink: #f4f4f4;
    --contact-ink: #f1b3b8;
  }
  * { margin: 0; padding: 0; box-sizing: border-box; }
  html, body {
    width: 1200px;
    height: 970px;
    overflow: hidden;
    background: var(--backdrop);
    font-family: "Roboto", Arial, sans-serif;
  }
  .card {
    position: absolute;
    left: 100px;
    top: 201px;
    width: 1000px;
    height: 568px;
    border-radius: 34px;
    overflow: hidden;
    background: linear-gradient(180deg, var(--card-top) 0%, var(--card-top-edge) 100%);
    box-shadow: 0 14px 40px rgba(0, 0, 0, 0.18);
  }
  .card__brand {
    position: absolute;
    top: 0;
    left: 0;
    right: 0;
    height: 327px;
    display: flex;
    align-items: center;
    justify-content: center;
  }
  .brand-name {
    font-weight: 500;
    font-size: 66px;
    color: var(--logo-ink);
    letter-spacing: 1px;
  }
  .card__name-band {
    position: absolute;
    top: 327px;
    left: 0;
    right: 0;
    height: 56px;
    background: linear-gradient(180deg, var(--band-grey-light) 0%, var(--band-grey-dark) 100%);
    display: flex;
    align-items: center;
    justify-content: center;
    color: var(--name-ink);
  }
  .person-name {
    font-weight: 500;
    font-size: 32px;
    letter-spacing: 0.5px;
  }
  .divider {
    width: 2px;
    height: 36px;
    background: var(--name-ink);
    margin: 0 12px;
    opacity: 0.8;
  }
  .person-role {
    font-weight: 400;
    font-size: 25px;
  }
  .card__contact {
    position: absolute;
    top: 383px;
    left: 0;
    right: 0;
    bottom: 0;
    background: linear-gradient(180deg, var(--blue-light) 0%, var(--blue-dark) 100%);
    display: flex;
    flex-direction: column;
    align-items: center;
    padding-top: 42px;
    color: var(--contact-ink);
    font-size: 25px;
    line-height: 33px;
  }
</style>
</head>
<body>
  <div class="card">
    <div class="card__brand">
      <span class="brand-name">Brambury Logistics</span>
    </div>
    <div class="card__name-band">
      <span class="person-name">TOMAS VARNELL</span>
      <span class="divider"></span>
      <span class="person-role">Manager</span>
    </div>
    <div class="card__contact">
      <span class="contact-phone">0400 123 456</span>
      <span class="contact-email">tomas@bramburylogistics.com.au</span>
      <span class="contact-web">www.bramburylogistics.com.au</span>
    </div>
  </div>
</body>
</html>
```